Exciting new branding of Recruitment Company based on it's new website

We have an exciting new website we are about to launch and would like to have letterhead, business cards, email signature options, email banner, linkedin and facebook cover images all refreshed to match the website. I have attached the existing logo. The website is at http://brightcrewstaff.hostpadsites.com/ and we are particularly interested in the grey with orange writing at the base of the first page where it says Register Now

Target Market(s)

Recruitment

Contact Information for Business Card

Dana Thorpe
Account Executive
T: 1300 582 318
M: 0412 736 085
E: dana@brightcrewstaff.com.au
W: brightcrewstaff.com.au
A: Suite 3, 42 Wattlebank Lane, Deakin ACT 2600
ABN: 52 184 637 905

Font styles to use
Serif
Sans Serif

Requirements
Must have
• The grey colour from the website

```html
<!DOCTYPE html>
<html lang="en">
<head>
<meta charset="utf-8">
<title>Brightcrew Staff – Stationery</title>
<link href="https://fonts.googleapis.com/css2?family=Signika:wght@300;400;600&display=swap" rel="stylesheet">
<style>
:root{
  --orange:#f7941d;
  --orange-soft:#fbb46a;
  --ink:#4a4a4a;
  --paper:#ffffff;
  --backdrop:#e2e2e2;
  --rule:#dcdcdc;
}
*{margin:0;padding:0;box-sizing:border-box}
html,body{width:1200px;height:1200px;overflow:hidden}
body{background:var(--backdrop);font-family:"Signika",sans-serif;color:var(--ink);position:relative}

.brand{display:flex;align-items:center;gap:8px;color:var(--orange);font-weight:600;line-height:.95}
.brand-mark{border:3px solid var(--orange);border-radius:50%;flex:none}
.brand-name{display:block}

.letterhead{position:absolute;left:336px;top:93px;width:528px;height:769px;background:var(--paper)}
.letterhead .brand{position:absolute;left:200px;top:35px}
.letterhead .brand-mark{width:60px;height:60px}
.letterhead .brand-name{font-size:16px}
.letterhead-address{position:absolute;top:702px;left:0;width:100%;text-align:center;font-size:8.5px;font-weight:600}
.letterhead-rule{position:absolute;top:718px;left:64px;width:400px;border-top:1px solid var(--rule)}
.letterhead-contacts{position:absolute;top:722px;left:0;width:100%;text-align:center;font-size:9.3px;font-weight:600;white-space:nowrap;letter-spacing:-.1px}
.label{color:var(--orange)}
.letterhead-band{position:absolute;bottom:0;left:0;width:100%;height:24px;background:var(--orange)}

.card{position:absolute;top:921px;width:300px;height:170px}
.card-front{left:271px;background:var(--paper)}
.card-front .brand{position:absolute;left:20px;top:19px;gap:6px}
.card-front .brand-mark{width:44px;height:44px;border-width:2px}
.card-front .brand-name{font-size:12.5px}
.card-person{position:absolute;left:154px;top:28px}
.card-name{font-size:13px;font-weight:400;color:var(--orange)}
.card-role{font-size:7px;font-weight:600;margin-top:3px}
.card-contacts{position:absolute;left:154px;top:104px;list-style:none;font-size:7.5px;font-weight:600;line-height:14.3px}
.card-contacts .label{display:inline-block;width:12px}
.card-address{position:absolute;left:20px;top:130px;font-size:7.5px;font-weight:600;line-height:13px;font-style:normal}

.card-back{left:630px;width:299px;background:radial-gradient(ellipse 60% 65% at 50% 50%,#fff 25%,var(--orange-soft) 75%,var(--orange) 100%)}
.card-back .brand{position:absolute;left:70px;top:50px;gap:10px}
.card-back .brand-mark{width:66px;height:66px;border-width:3px}
.card-back .brand-name{font-size:18px}
</style>
</head>
<body>

<section class="letterhead">
  <div class="brand">
    <span class="brand-mark"></span>
    <span class="brand-name">brightcrew<br>staff</span>
  </div>
  <p class="letterhead-address">Suite 3, 42 Wattlebank Lane, Hollowmere ACT 2619</p>
  <div class="letterhead-rule"></div>
  <p class="letterhead-contacts"><span class="label">T</span> : 1300 582 318 | <span class="label">M</span> : 0412 736 085 | <span class="label">W:</span> brightcrewstaff.com.au | <span class="label">E:</span> dana@brightcrewstaff.com.au | <span class="label">ABN</span> : 52 184 637 905</p>
  <div class="letterhead-band"></div>
</section>

<section class="card card-front">
  <div class="brand">
    <span class="brand-mark"></span>
    <span class="brand-name">brightcrew<br>staff</span>
  </div>
  <div class="card-person">
    <p class="card-name">Dana Thorpe</p>
    <p class="card-role">Account Executive</p>
  </div>
  <ul class="card-contacts">
    <li><span class="label">T</span>: 1300 582 318</li>
    <li><span class="label">M</span>: 0412 736 085</li>
    <li><span class="label">W</span>: brightcrewstaff.com.au</li>
    <li><span class="label">E</span>: dana@brightcrewstaff.com.au</li>
  </ul>
  <address class="card-address">Suite 3, 42 Wattlebank Lane,<br>Hollowmere ACT 2619</address>
</section>

<section class="card card-back">
  <div class="brand">
    <span class="brand-mark"></span>
    <span class="brand-name">brightcrew<br>staff</span>
  </div>
</section>

</body>
</html>
```